Realty Group Needs Classy, Contemporary Letterhead Design

We need a letterhead design for a new realty company located in NY, USA. We buy investment properties to rehabilitate and or keep in our rental portfolio.

```html
<!DOCTYPE html>
<html lang="en">
<head>
<meta charset="utf-8">
<title>Meridian Realty Group – Letterhead</title>
<link rel="stylesheet" href="https://fonts.googleapis.com/css2?family=Montserrat:wght@800&family=Open+Sans:wght@600;700&display=swap">
<style>
  :root {
    --brand-purple: #4f2a83;
    --rule-gray: #9a9a9a;
    --text-gray: #b4b4b4;
    --paper: #ffffff;
    --backdrop: #dcdcdc;
    --shadow: rgba(0, 0, 0, 0.45);
  }
  * { margin: 0; padding: 0; box-sizing: border-box; }
  html, body { width: 1200px; height: 762px; overflow: hidden; background: var(--backdrop); }
  .stage { position: relative; width: 1200px; height: 762px; }

  .sheet {
    position: absolute;
    top: 97px;
    width: 440px;
    height: 570px;
    background: var(--paper);
    box-shadow: 10px 10px 18px var(--shadow);
    overflow: hidden;
  }
  .sheet--blank { left: 96px; }
  .sheet--letter { left: 646px; }

  .sheet__frame { position: absolute; inset: 0; width: 440px; height: 570px; }
  .band { fill: var(--brand-purple); }
  .rule { fill: none; stroke: var(--rule-gray); stroke-width: 3; }

  .brand {
    position: absolute;
    left: 23px;
    top: 22px;
    font-family: "Montserrat", sans-serif;
    font-weight: 800;
    color: var(--brand-purple);
    line-height: 1;
  }
  .brand__name { display: block; font-size: 24px; letter-spacing: -0.5px; }
  .brand__sub { display: block; font-size: 8.5px; letter-spacing: 0.6px; margin-top: 2px; padding-left: 34px; }

  .letter { position: absolute; left: 41px; top: 154px; width: 370px; font-family: "Open Sans", sans-serif; }
  .letter__heading { font-size: 11.5px; font-weight: 700; color: var(--brand-purple); margin-bottom: 12px; }
  .letter__body {
    font-size: 7.4px;
    font-weight: 700;
    line-height: 10.4px;
    color: var(--text-gray);
    margin-bottom: 12px;
  }

  .sign-off { position: absolute; left: 316px; top: 320px; width: 82px; font-family: "Open Sans", sans-serif; }
  .sign-off__label { font-size: 5.6px; font-weight: 700; color: var(--text-gray); text-align: center; margin-bottom: 4px; }
  .sign-off__signature { height: 10px; background: linear-gradient(#ffffff 40%, #d9d9d9 50%, #ffffff 60%); }
</style>
</head>
<body>
<main class="stage">

  <section class="sheet sheet--blank" aria-label="Blank letterhead">
    <svg class="sheet__frame" viewBox="0 0 440 570" aria-hidden="true">
      <path class="band" d="M170 0 C186 0 192 16 202 28 C210 38 220 42 238 42 L440 42 L440 0 Z"/>
      <path class="rule" d="M204 45 C212 49 220 50 236 50 L440 50"/>
      <path class="band" d="M0 546 L200 546 C238 546 262 556 272 570 L0 570 Z"/>
    </svg>
    <div class="brand">
      <span class="brand__name">MERIDIAN</span>
      <span class="brand__sub">Realty Group, LLC</span>
    </div>
  </section>

  <section class="sheet sheet--letter" aria-label="Letterhead with sample letter">
    <svg class="sheet__frame" viewBox="0 0 440 570" aria-hidden="true">
      <path class="band" d="M170 0 C186 0 192 16 202 28 C210 38 220 42 238 42 L440 42 L440 0 Z"/>
      <path class="rule" d="M204 45 C212 49 220 50 236 50 L440 50"/>
      <path class="band" d="M0 546 L200 546 C238 546 262 556 272 570 L0 570 Z"/>
    </svg>
    <div class="brand">
      <span class="brand__name">MERIDIAN</span>
      <span class="brand__sub">Realty Group, LLC</span>
    </div>

    <article class="letter">
      <h1 class="letter__heading">Realty Group</h1>
      <p class="letter__body">Real estate company introduction letter is the most cost-effective method you can use to introduce your company. Prospects in general, don’t wish to work with the company which has no exposure. So it is important that the prospect knows your company and has been receiving your messages often. In real estate, in order to develop regular communication with your potential prospect, it is vital that you get an excellent head start over your competitors.</p>
      <p class="letter__body">Real estate company introduction letter is the most cost-effective method you can use to introduce your company. Prospects in general, don’t wish to work with the company which has no exposure. So it is important that the prospect knows your company and has been receiving your messages often. In real estate, in order to develop regular communication with your potential prospect, it is vital that you get an excellent head start over your competitors.</p>
    </article>

    <div class="sign-off">
      <p class="sign-off__label">Realty Group</p>
      <div class="sign-off__signature" role="img" aria-label="Handwritten signature"></div>
    </div>
  </section>

</main>
</body>
</html>
```